Stationary Design

Harbor Stagecraft Collective, Inc
27410 Marlowe Blvd Ste 4, Cedar Hollow, CA 90512
Office: 213-584-2760 Email: admin@hsccrew.example

Industry/Entity Type

Entertainment

Colors
0054AA
0677BA
7BADD7
CADEEF
E8F1F8

```html
<!DOCTYPE html>
<html lang="en">
<head>
<meta charset="utf-8">
<title>Harbor Stagecraft Collective — Stationery</title>
<link href="https://fonts.googleapis.com/css2?family=Roboto:wght@300;400;500;700&display=swap" rel="stylesheet">
<style>
:root{
  --blue:#0054AA;
  --blue-mid:#0677BA;
  --blue-soft:#7BADD7;
  --blue-pale:#CADEEF;
  --blue-mist:#E8F1F8;
  --paper:#F5F3F4;
  --white:#FFFFFF;
  --ink:#3b3b3b;
  --grey:#8c8f94;
  --stage:#3a3b3d;
}
*{margin:0;padding:0;box-sizing:border-box}
html,body{width:1200px;height:597px;overflow:hidden;background:var(--stage);font-family:'Roboto',Arial,sans-serif;color:var(--ink)}
.canvas{position:relative;width:1200px;height:597px}
.piece{position:absolute;overflow:hidden}

/* wordmark */
.wordmark{display:flex;flex-direction:column;align-items:center;gap:3px}
.wordmark .dot{border-radius:50%;background:var(--blue)}
.wordmark .name{font-weight:500;color:var(--blue);white-space:nowrap;letter-spacing:.02em}

.contact,.sender{font-size:5.6px;line-height:7.4px;color:var(--ink)}
.row{display:flex;align-items:center;gap:4px}
.gap{height:4px}
.icon{width:5px;height:5px;flex:none}

/* business card front */
.card-front{left:45px;top:120px;width:255px;height:146px;background:var(--white);border-radius:6px}
.card-front .wordmark{position:absolute;left:10px;top:46px;width:122px}
.card-front .dot{width:26px;height:26px}
.card-front .name{font-size:8.5px}
.card-front .divider{position:absolute;left:135px;top:34px;width:1px;height:78px;background:#d8d8d8}
.card-front .person{position:absolute;left:146px;top:37px}
.card-front .person h2{font-size:10px;font-weight:700;color:var(--blue);letter-spacing:.03em}
.card-front .person .role{font-size:5.6px;color:var(--grey);margin-top:2px}
.card-front .contact{position:absolute;left:146px;top:62px}
.card-front .contact .gap{height:5px}
.card-front .rule{position:absolute;left:0;right:0;top:138px;height:1px;background:var(--grey)}
.card-front .band{position:absolute;left:0;right:0;top:140px;height:6px;background:var(--blue)}

/* business card back */
.card-back{left:39px;top:322px;width:261px;height:149px;background:var(--blue);border-radius:7px}
.card-back .wordmark{position:absolute;left:0;right:0;top:46px}
.card-back .dot{width:40px;height:40px;background:var(--blue-mid)}
.card-back .name{font-size:13px;color:var(--white)}

/* letterhead */
.letterhead{left:345px;top:61px;width:358px;height:504px;background:var(--paper)}
.letterhead .wordmark{position:absolute;left:22px;top:34px;width:72px}
.letterhead .dot{width:22px;height:22px}
.letterhead .name{font-size:6px}
.letterhead .sender{position:absolute;left:255px;top:34px}
.letterhead .ghost{position:absolute;left:80px;top:135px;width:200px;height:200px;border-radius:50%;background:var(--blue-mist);opacity:.8}
.letterhead .letter{position:absolute;left:26px;top:124px;width:311px}
.letter .salutation{font-size:10px;font-weight:400;color:#444;margin-bottom:14px}
.letter p{font-size:5.1px;line-height:8.6px;color:#555;text-align:justify;margin-bottom:8.6px;position:relative}
.letter .closing{font-size:5.4px;color:#555;margin-top:16px}
.letter .signature{width:48px;height:20px;margin:12px 0 0 8px;background:var(--blue-pale);opacity:.5;border-radius:2px}
.letter .signer{margin:6px 0 0 11px;font-size:7.6px;color:#444}
.letter .signer-role{margin:2px 0 0 11px;font-size:5.6px;color:#666}
.letterhead .rule{position:absolute;left:0;right:0;top:490px;height:1.5px;background:var(--grey)}
.letterhead .band{position:absolute;left:0;right:0;top:494px;height:10px;background:var(--blue);color:var(--white);font-size:5.6px;text-align:center;line-height:10px}

/* envelope */
.envelope-back{left:758px;top:200px;width:402px;height:183px;background:var(--paper)}
.envelope-back svg{position:absolute;left:0;top:0}
.envelope-back .flap-name{position:absolute;left:0;right:0;top:27px;text-align:center;font-size:11px;font-weight:500;color:var(--white);letter-spacing:.02em}
.envelope-front{left:728px;top:297px;width:403px;height:184px;background:var(--paper);box-shadow:0 2px 6px rgba(0,0,0,.25)}
.envelope-front .wordmark{position:absolute;left:16px;top:16px;width:72px}
.envelope-front .dot{width:22px;height:22px}
.envelope-front .name{font-size:6px}
.envelope-front .ghost{position:absolute;left:225px;top:8px;width:170px;height:170px;border-radius:50%;background:var(--blue-mist)}
.envelope-front .sender{position:absolute;left:18px;top:118px}
.envelope-front .sender .gap{height:5px}
.envelope-front .rule{position:absolute;left:0;right:0;top:169px;height:1.5px;background:var(--grey)}
.envelope-front .band{position:absolute;left:0;right:0;top:173px;height:11px;background:var(--blue);color:var(--white);font-size:5.6px;text-align:center;line-height:11px}
</style>
</head>
<body>
<div class="canvas">

  <section class="piece card-front">
    <div class="wordmark"><span class="dot"></span><span class="name">Harbor Stagecraft</span></div>
    <div class="divider"></div>
    <div class="person">
      <h2>DANA WHITFIELD</h2>
      <div class="role">President</div>
    </div>
    <div class="contact">
      <div>Harbor Stagecraft Collective, Inc</div>
      <div>27410 Marlowe Blvd Ste 4,</div>
      <div>Cedar Hollow, CA 90512</div>
      <div class="gap"></div>
      <div class="row"><svg class="icon" viewBox="0 0 10 10"><path d="M2 1l2 0 1 2.5-1.2 1a6 6 0 0 0 2.7 2.7l1-1.2L10 7v2c-5 .5-9-3.5-8-8z" fill="#0054AA"/></svg>213-584-2760</div>
      <div class="row"><svg class="icon" viewBox="0 0 10 10"><rect x="0.5" y="2" width="9" height="6" fill="#0054AA"/><path d="M.5 2l4.5 3.5L9.5 2" stroke="#fff" fill="none"/></svg>admin@hsccrew.example</div>
      <div class="row"><svg class="icon" viewBox="0 0 10 10"><circle cx="5" cy="5" r="4.5" fill="#0054AA"/><path d="M.5 5h9M5 .5c-2 2.5-2 6.5 0 9M5 .5c2 2.5 2 6.5 0 9" stroke="#fff" stroke-width=".7" fill="none"/></svg>www.hsccrew.example</div>
    </div>
    <div class="rule"></div>
    <div class="band"></div>
  </section>

  <section class="piece card-back">
    <div class="wordmark"><span class="dot"></span><span class="name">Harbor Stagecraft</span></div>
  </section>

  <section class="piece letterhead">
    <div class="ghost"></div>
    <div class="wordmark"><span class="dot"></span><span class="name">Harbor Stagecraft</span></div>
    <div class="sender">
      <div>Harbor Stagecraft Collective, Inc</div>
      <div>27410 Marlowe Blvd Ste 4</div>
      <div>Cedar Hollow, CA 90512</div>
      <div class="gap"></div>
      <div class="row"><svg class="icon" viewBox="0 0 10 10"><rect x="2.5" y=".5" width="5" height="9" rx="1" fill="none" stroke="#0054AA"/></svg>213-584-2760</div>
      <div class="row"><svg class="icon" viewBox="0 0 10 10"><rect x="0.5" y="2" width="9" height="6" fill="#0054AA"/><path d="M.5 2l4.5 3.5L9.5 2" stroke="#fff" fill="none"/></svg>admin@hsccrew.example</div>
    </div>
    <article class="letter">
      <h1 class="salutation">Dear Mr. Whitfield,</h1>
      <p>Lorem ipsum dolor sit amet, consectetur adipiscing elit. Donec orci purus, luctus vitae dignissim eu, iaculis sed purus. Vivamus faucibus, ipsum nec aliquet viverra, leo mauris condimentum ligula, sit amet sagittis enim ligula quis arcu. Nam egestas tortor id nisi porttitor mattis. In tortor ante, ultricies in suscipit a, tempus non massa. Vivamus et auctor mi. Fusce vel massa nulla. Phasellus nec eros mauris, et scelerisque orci.</p>
      <p>Donec malesuada orci vitae nulla accumsan porta a id massa. Quisque accumsan iaculis magna sit amet fringilla. Maecenas consequat, magna eget tincidunt semper, odio nibh rutrum mi, id feugiat ante nisi eu risus. Vestibulum nunc orci, rhoncus a placerat in, ultricies in mi. Cras mattis varius eros, vel fringilla nisi suscipit eget. Quisque scelerisque sagittis nulla at porttitor.</p>
      <p>Sed id augue vitae urna euismod commodo aliquet a quam. Pellentesque arcu velit, cursus et malesuada ut, consequat et diam. Nullam erat sem, rhoncus id ullamcorper vitae, rhoncus et arcu. In ultricies ultricies nulla, ut rutrum nisi iaculis at. Donec eu magna a metus ornare faucibus. Fusce aliquet faucibus ultricies. Morbi semper, est id tincidunt gravida, sem arcu adipiscing lacus, ac bibendum nulla leo eu purus. Quisque nec diam sed risus consectetur a ccumsan quis quis nibh. Vestibulum id purus lorem.</p>
      <p>It is a long established fact that a reader will be distracted by the readable content of a page when looking at its layout. The point of using Lorem Ipsum is that it has a more-or-less normal distribution of letters, as opposed to using 'Content here, content here', making it look like readable English. Many desktop publishing packages</p>
      <div class="closing">Sincerely,</div>
      <div class="signature" role="img" aria-label="Handwritten signature"></div>
      <div class="signer">Dana Whitfield</div>
      <div class="signer-role">CEO/ Founder</div>
    </article>
    <div class="rule"></div>
    <div class="band">www.hsccrew.example</div>
  </section>

  <section class="piece envelope-back">
    <svg width="402" height="70" viewBox="0 0 402 70">
      <path d="M0 0H402L396 42Q393 67 368 67H34Q9 67 6 42Z" fill="#0054AA"/>
    </svg>
    <div class="flap-name">Harbor Stagecraft</div>
  </section>

  <section class="piece envelope-front">
    <div class="ghost"></div>
    <div class="wordmark"><span class="dot"></span><span class="name">Harbor Stagecraft</span></div>
    <div class="sender">
      <div>Harbor Stagecraft Collective, Inc</div>
      <div>27410 Marlowe Blvd Ste 4</div>
      <div>Cedar Hollow, CA 90512</div>
      <div class="gap"></div>
      <div class="row"><svg class="icon" viewBox="0 0 10 10"><rect x="2.5" y=".5" width="5" height="9" rx="1" fill="none" stroke="#0054AA"/></svg>213-584-2760</div>
      <div class="row"><svg class="icon" viewBox="0 0 10 10"><rect x="0.5" y="2" width="9" height="6" fill="#0054AA"/><path d="M.5 2l4.5 3.5L9.5 2" stroke="#fff" fill="none"/></svg>admin@hsccrew.example</div>
    </div>
    <div class="rule"></div>
    <div class="band">www.hsccrew.example</div>
  </section>

</div>
</body>
</html>
```